Website Service Icon Design

We need a set of icons designed to represent products and product categories to be used on a website and in offline promotional material.

The required icons are:
- Website Hosting
- Internet Connectivity
- Domain Names
- Managed Services
- Fibre Optic Services
- High Speed Services
- Corporate Services
- Telephone Services
- Fax Services
- Voice over IP Services
Updates

Project Deadline Extended
Reason: Extended until after the holiday period.

Target Market(s)

Target market is medium to large corporate customers.

Industry/Entity Type

It Service

Requirements
Must have
• Black on white flat colour designs only, with one optional accent colour.
Should not have
• No shadows or gradients. No text.

```html
<!DOCTYPE html>
<html lang="en">
<head>
<meta charset="utf-8">
<title>Service Icons</title>
<link rel="stylesheet" href="https://fonts.googleapis.com/css2?family=Josefin+Sans:wght@400;600&family=Montserrat:wght@500&display=swap">
<style>
  :root {
    --bg: #f8f9fb;
    --ink: #1e2a35;
    --accent: #3a8fd6;
    --badge: #ffd200;
    --white: #ffffff;
  }
  html, body {
    margin: 0;
    padding: 0;
    overflow: hidden;
    background: var(--bg);
  }
  .canvas {
    position: relative;
    width: 1200px;
    height: 900px;
    overflow: hidden;
    background: var(--bg);
  }
  .corner-badge {
    position: absolute;
    top: 0;
    right: 0;
    width: 190px;
    height: 190px;
  }
  .corner-badge__number {
    position: absolute;
    top: 26px;
    right: 30px;
    font-family: "Josefin Sans", sans-serif;
    font-weight: 400;
    font-size: 60px;
    line-height: 1;
    color: var(--white);
  }
  .service-icon {
    position: absolute;
  }
  .service-label {
    position: absolute;
    left: 464px;
    margin: 0;
    font-family: "Josefin Sans", sans-serif;
    font-weight: 400;
    font-size: 31px;
    letter-spacing: 1.5px;
    line-height: 1;
    color: var(--ink);
    text-transform: uppercase;
    transform: translateY(-50%);
  }
  .label-hosting { top: 212px; }
  .label-connectivity { top: 484px; }
  .label-domains { top: 740px; }
  .domain-mark {
    position: absolute;
    left: 158px;
    top: 704px;
    height: 64px;
    display: flex;
    align-items: center;
    font-family: "Montserrat", sans-serif;
    font-weight: 500;
    font-size: 52px;
    letter-spacing: 1px;
    color: var(--ink);
  }
  .domain-mark__cursor {
    display: inline-block;
    width: 6px;
    height: 64px;
    margin-left: 6px;
    background: var(--accent);
  }
</style>
</head>
<body>
<main class="canvas">
  <div class="corner-badge">
    <svg width="190" height="190" viewBox="0 0 190 190" aria-hidden="true">
      <polygon points="0,0 190,0 190,190" fill="var(--badge)"/>
    </svg>
    <span class="corner-badge__number">1</span>
  </div>

  <svg class="service-icon icon-cloud" style="left:130px;top:100px" width="230" height="170" viewBox="0 0 230 170" aria-hidden="true">
    <path d="M48 158 H178 A42 42 0 0 0 180 74 A44 44 0 0 0 128 48 A62 62 0 0 0 42 84 A38 38 0 0 0 48 158 Z"
          fill="none" stroke="var(--ink)" stroke-width="10" stroke-linejoin="round"/>
  </svg>
  <p class="service-label label-hosting">Website Hosting</p>

  <svg class="service-icon icon-port" style="left:148px;top:386px" width="188" height="188" viewBox="0 0 188 188" aria-hidden="true">
    <circle cx="94" cy="94" r="94" fill="var(--ink)"/>
    <path d="M42 60 H54 V48 H134 V60 H146 V132 H42 Z" fill="var(--white)" stroke="var(--white)" stroke-width="4" stroke-linejoin="round"/>
    <g stroke="var(--accent)" stroke-width="5">
      <line x1="76" y1="90" x2="76" y2="114"/>
      <line x1="90" y1="90" x2="90" y2="114"/>
      <line x1="104" y1="90" x2="104" y2="114"/>
      <line x1="118" y1="90" x2="118" y2="114"/>
    </g>
  </svg>
  <p class="service-label label-connectivity">Internet Connectivity</p>

  <div class="service-icon domain-mark">www.<span class="domain-mark__cursor"></span></div>
  <p class="service-label label-domains">Domain Names</p>
</main>
</body>
</html>
```